Mobile Crushing and Screening

Please design A5 double sided flyer, one side for Crusher other for screener. Please use photos, logo and wording in word document.
Main colours are Dark Green: #0B5D2A
Light Green: #8BC34A
please see our website www.brightridgeplant.com.au
Thank you

Requirements
Must have
• colour scheme as in website

```html
<!DOCTYPE html>
<html lang="en">
<head>
<meta charset="utf-8">
<title>Brightridge Plant – Mobile Crushing &amp; Screening Flyers</title>
<link href="https://fonts.googleapis.com/css2?family=Montserrat:wght@600;700;800;900&family=Roboto+Condensed:wght@400;700&family=Oswald:wght@600&display=swap" rel="stylesheet">
<style>
  :root{
    --dark-green:#0B5D2A;
    --light-green:#8BC34A;
    --white:#ffffff;
    --ink:#1d1d1d;
    --backdrop:#e9ebe8;
    --photo-sky:#9aa88a;
    --photo-ground:#8c7a62;
  }
  *{box-sizing:border-box;margin:0;padding:0}
  html,body{width:1200px;height:775px;overflow:hidden;background:var(--backdrop)}
  body{position:relative;font-family:"Montserrat",sans-serif;color:var(--ink)}

  .flyer{position:absolute;top:40px;width:490px;height:694px;background:var(--white);overflow:hidden;box-shadow:0 6px 18px rgba(0,0,0,.18)}
  .flyer--crusher{left:80px}
  .flyer--screener{left:630px}

  .hero-photo{position:absolute;left:0;top:0;width:100%;height:380px;
    background:linear-gradient(180deg,var(--photo-sky) 0%,#7f8d6c 40%,var(--photo-ground) 100%)}
  .flyer--screener .hero-photo{background:linear-gradient(180deg,#8e9c7c 0%,#9a8568 55%,#7d6850 100%)}

  .brand-oval{position:absolute;top:-22px;width:250px;height:128px;border-radius:50%;background:var(--white);
    border:4px solid var(--light-green);display:flex;flex-direction:column;align-items:center;justify-content:center;padding-top:18px}
  .flyer--crusher .brand-oval{right:10px}
  .flyer--screener .brand-oval{left:10px}
  .brand-name{display:flex;align-items:center;gap:6px;font-weight:900;font-size:17px;color:var(--dark-green);letter-spacing:.3px;white-space:nowrap}
  .brand-name i{display:block;flex:none;width:11px;height:11px;border-radius:50%;background:var(--light-green)}
  .brand-tag{font-size:6.5px;font-weight:700;letter-spacing:2.4px;color:var(--dark-green);margin-top:4px;white-space:nowrap}

  .curve{position:absolute;left:0;top:0;width:490px;height:694px}

  .headline{position:absolute;left:0;width:100%;text-align:center;color:var(--dark-green);font-weight:900;line-height:1.05}
  .headline .small{display:block;font-size:27px}
  .headline .big{display:block;font-size:31px}
  .flyer--crusher .headline,.flyer--screener .headline{top:232px}

  .banner{position:absolute;left:50%;transform:translateX(-50%);height:26px;background:var(--light-green);
    color:var(--white);font-weight:900;font-size:19px;display:flex;align-items:center;justify-content:center;
    clip-path:polygon(0 0,100% 0,92% 100%,8% 100%);letter-spacing:.5px;z-index:2;white-space:nowrap}

  .frame{position:absolute;left:20px;right:20px;border:2px solid var(--light-green);border-radius:8px;background:var(--white)}

  .tile-row{position:absolute;display:flex;gap:5px}
  .tile{width:80px;height:100px;border:2px solid var(--light-green);border-radius:6px;background:var(--white);
    display:flex;flex-direction:column;align-items:center;justify-content:center;gap:8px}
  .tile svg{width:42px;height:42px;fill:var(--dark-green)}
  .tile-label{font-family:"Roboto Condensed",sans-serif;font-weight:700;font-size:13px;color:var(--ink);text-align:center;line-height:1.05}
  .tile-note{display:block;font-weight:400;font-size:8px;margin-top:2px}

  .capability{position:absolute;left:20px;right:20px;top:508px;height:92px}
  .capability ul{list-style:none;display:flex;gap:16px;padding:22px 14px 0 14px}
  .capability li{display:flex;gap:6px;font-size:10.5px;font-weight:600;line-height:1.35;flex:1}
  .capability li b{font-weight:800}
  .tick{flex:none;width:13px;height:13px;margin-top:1px}

  .separation{position:absolute;left:0;width:100%;text-align:center;font-weight:800;font-size:12.5px;color:var(--ink)}

  .footer{position:absolute;left:0;bottom:0;width:100%;height:66px;background:var(--dark-green);display:flex;align-items:center;justify-content:space-between;padding:0 12px 0 0}
  .quote-pill{flex:none;height:40px;background:var(--light-green);border-radius:0 20px 20px 0;display:flex;align-items:center;gap:7px;padding:0 14px 0 16px;
    font-family:"Oswald",sans-serif;font-weight:600;color:var(--dark-green);white-space:nowrap}
  .quote-pill .cta{font-size:16px;margin-right:3px}
  .quote-pill .phone{font-size:18px}
  .quote-pill svg{flex:none;width:17px;height:17px}
  .contacts{flex:none;list-style:none;color:var(--white);font-size:10px;font-weight:600;line-height:1.6;white-space:nowrap}
  .contacts li{display:flex;align-items:center;gap:5px}
  .contacts svg{flex:none;width:11px;height:11px;fill:none;stroke:var(--light-green);stroke-width:2}
</style>
</head>
<body>

<svg width="0" height="0" style="position:absolute" aria-hidden="true">
  <defs>
    <symbol id="icon-concrete" viewBox="0 0 40 40"><rect x="4" y="6" width="30" height="28" rx="1"/><path d="M14 6v28M24 6v28M4 16h30M4 26h30" stroke="#fff" stroke-width="1.6"/><rect x="2" y="33" width="36" height="4"/></symbol>
    <symbol id="icon-brick" viewBox="0 0 40 40"><rect x="12" y="6" width="16" height="7"/><rect x="4" y="15" width="15" height="7"/><rect x="21" y="15" width="15" height="7"/><rect x="0" y="24" width="12" height="7"/><rect x="14" y="24" width="12" height="7"/><rect x="28" y="24" width="12" height="7"/><rect x="8" y="33" width="24" height="5"/></symbol>
    <symbol id="icon-blocks" viewBox="0 0 40 40"><path d="M20 4l8 4v8l-8 4-8-4V8z"/><path d="M11 17l8 4v8l-8 4-8-4v-8z"/><path d="M29 17l8 4v8l-8 4-8-4v-8z"/></symbol>
    <symbol id="icon-roller" viewBox="0 0 40 40"><rect x="8" y="4" width="20" height="3"/><rect x="9" y="7" width="2" height="12"/><rect x="25" y="7" width="2" height="12"/><rect x="6" y="18" width="28" height="8"/><circle cx="11" cy="31" r="6"/><rect x="20" y="26" width="16" height="10" rx="2"/></symbol>
    <symbol id="icon-stone" viewBox="0 0 40 40"><path d="M4 24l8-12 14-6 10 10-2 14-16 4-12-4z"/><path d="M10 22l12-2 10 6" stroke="#fff" stroke-width="1.6" fill="none"/></symbol>
    <symbol id="icon-soil" viewBox="0 0 40 40"><path d="M2 8q6-3 12 0t12 0 12 0v4H2z"/><rect x="2" y="14" width="36" height="8"/><rect x="2" y="24" width="36" height="5"/><rect x="2" y="31" width="36" height="5"/><circle cx="10" cy="18" r="1.5" fill="#fff"/><circle cx="24" cy="18" r="1.5" fill="#fff"/></symbol>
    <symbol id="icon-sand" viewBox="0 0 40 40"><path d="M2 34L14 8l12 26z"/><path d="M18 34l10-16 11 16z"/><rect x="2" y="34" width="37" height="3"/></symbol>
    <symbol id="icon-gravel" viewBox="0 0 40 40"><circle cx="12" cy="11" r="6"/><circle cx="26" cy="10" r="5"/><circle cx="8" cy="24" r="5"/><circle cx="20" cy="23" r="6"/><circle cx="32" cy="22" r="5"/><circle cx="14" cy="34" r="4"/><circle cx="27" cy="33" r="4"/></symbol>
    <symbol id="icon-construction" viewBox="0 0 40 40"><rect x="8" y="8" width="3" height="30"/><rect x="2" y="6" width="28" height="3"/><rect x="26" y="9" width="1.5" height="8"/><rect x="20" y="18" width="16" height="20"/><rect x="23" y="22" width="3" height="3" fill="#fff"/><rect x="30" y="22" width="3" height="3" fill="#fff"/><rect x="23" y="29" width="3" height="3" fill="#fff"/><rect x="30" y="29" width="3" height="3" fill="#fff"/></symbol>
    <symbol id="icon-tick" viewBox="0 0 14 14"><circle cx="7" cy="7" r="7" fill="#0B5D2A"/><path d="M3.8 7.2l2.2 2.2 4.2-4.4" stroke="#fff" stroke-width="1.8" fill="none"/></symbol>
    <symbol id="icon-phone" viewBox="0 0 20 20"><circle cx="10" cy="10" r="9.5" fill="#0B5D2A"/><path d="M7 5.5l2 2.2-1 1.3q1 2 3 3l1.3-1 2.2 2-1.2 1.5q-3 .2-5.8-2.6T5.6 6.7z" fill="#8BC34A"/></symbol>
    <symbol id="icon-mail" viewBox="0 0 12 12"><rect x="1" y="2.5" width="10" height="7" rx="1"/><path d="M1 3l5 3.5L11 3"/></symbol>
    <symbol id="icon-web" viewBox="0 0 12 12"><circle cx="6" cy="6" r="5"/><path d="M1 6h10M6 1q-3 5 0 10M6 1q3 5 0 10"/></symbol>
  </defs>
</svg>

<section class="flyer flyer--crusher">
  <div class="hero-photo" role="img" aria-label="Photo of a tracked mobile jaw crusher with conveyor on a gravel site with scrub behind"></div>
  <div class="brand-oval">
    <div class="brand-name"><i></i>BRIGHTRIDGE PLANT</div>
    <div class="brand-tag">CRUSHING AND SCREENING</div>
  </div>
  <svg class="curve" viewBox="0 0 490 694" aria-hidden="true">
    <path d="M0 318 Q210 180 490 268 L490 694 L0 694 Z" fill="#fff"/>
    <path d="M0 306 Q210 166 490 256" fill="none" stroke="#8BC34A" stroke-width="6"/>
  </svg>
  <h1 class="headline"><span class="small">MOBILE</span><span class="big">CRUSHING SERVICES</span></h1>
  <div class="frame" style="top:356px;height:140px"></div>
  <div class="banner" style="top:318px;width:170px">WE CRUSH</div>
  <div class="tile-row" style="left:30px;top:376px">
    <div class="tile"><svg><use href="#icon-concrete"/></svg><span class="tile-label">Concrete</span></div>
    <div class="tile"><svg><use href="#icon-brick"/></svg><span class="tile-label">Brick</span></div>
    <div class="tile"><svg><use href="#icon-blocks"/></svg><span class="tile-label">Blocks</span></div>
    <div class="tile"><svg><use href="#icon-roller"/></svg><span class="tile-label">Asphalt</span></div>
    <div class="tile"><svg><use href="#icon-stone"/></svg><span class="tile-label">Natural stone<span class="tile-note">(sandstone, limestone &amp; more)</span></span></div>
  </div>
  <div class="frame capability">
    <ul>
      <li><svg class="tick"><use href="#icon-tick"/></svg><span><b>Production:</b> 5-50 tonnes per hour (dependent on feed &amp; output settings)</span></li>
      <li><svg class="tick"><use href="#icon-tick"/></svg><span>Maximum feed size of a single lump is 500mm x 280mm but for best performance <b>300mm material is preferred.</b></span></li>
    </ul>
  </div>
  <div class="banner" style="top:496px;width:330px">TECHNICAL CAPABILITY</div>
  <footer class="footer">
    <div class="quote-pill"><span class="cta">REQUEST A QUOTE</span><svg><use href="#icon-phone"/></svg><span class="phone">040 555 0182</span></div>
    <ul class="contacts">
      <li><svg><use href="#icon-mail"/></svg>info@brightridgeplant.com.au</li>
      <li><svg><use href="#icon-web"/></svg>www.brightridgeplant.com.au</li>
    </ul>
  </footer>
</section>

<section class="flyer flyer--screener">
  <div class="hero-photo" role="img" aria-label="Photo of a tracked mobile screener with side conveyors on a dirt site among gum trees"></div>
  <div class="brand-oval">
    <div class="brand-name"><i></i>BRIGHTRIDGE PLANT</div>
    <div class="brand-tag">CRUSHING AND SCREENING</div>
  </div>
  <svg class="curve" viewBox="0 0 490 694" aria-hidden="true">
    <path d="M0 330 Q200 170 490 250 L490 694 L0 694 Z" fill="#fff"/>
    <path d="M0 318 Q200 158 490 238" fill="none" stroke="#8BC34A" stroke-width="6"/>
  </svg>
  <h1 class="headline"><span class="small">MOBILE</span><span class="big">CRUSHING SERVICES</span></h1>
  <div class="frame" style="top:312px;height:296px"></div>
  <div class="banner" style="top:310px;width:170px">WE SCREEN</div>
  <div class="tile-row" style="left:120px;top:348px">
    <div class="tile"><svg><use href="#icon-concrete"/></svg><span class="tile-label">Concrete</span></div>
    <div class="tile"><svg><use href="#icon-brick"/></svg><span class="tile-label">Brick</span></div>
    <div class="tile"><svg><use href="#icon-stone"/></svg><span class="tile-label">Stone</span></div>
  </div>
  <div class="tile-row" style="left:34px;top:458px">
    <div class="tile"><svg><use href="#icon-soil"/></svg><span class="tile-label">Soil</span></div>
    <div class="tile"><svg><use href="#icon-sand"/></svg><span class="tile-label">Sand</span></div>
    <div class="tile"><svg><use href="#icon-gravel"/></svg><span class="tile-label">Gravel</span></div>
    <div class="tile" style="width:162px"><svg><use href="#icon-construction"/></svg><span class="tile-label">Other construction &amp;<br>demolition materials</span></div>
  </div>
  <p class="separation" style="top:578px">Accurate separation into fines, medium, and oversized</p>
  <footer class="footer">
    <div class="quote-pill"><span class="cta">REQUEST A QUOTE</span><svg><use href="#icon-phone"/></svg><span class="phone">040 555 0182</span></div>
    <ul class="contacts">
      <li><svg><use href="#icon-mail"/></svg>info@brightridgeplant.com.au</li>
      <li><svg><use href="#icon-web"/></svg>www.brightridgeplant.com.au</li>
    </ul>
  </footer>
</section>

</body>
</html>
```